IT supplier clean wordpress website - payment guaranteed

Clean website design for a wordpress based website
Design only - PSD delivery with images

current website: www.quilmo.net
please use your imagination and try something out of the box...
We like https://trevanly.com.au as look and feel, but you don't have to copy it, you can be creative

We like the navigation header and the phone number, but do not need 'instant quote' so the 1300 phone number and the 'lock' icon for login can be on the same line

Site Map:
IT support
VoIP
Internet and Data
Cloud hosting
About
Contact

Our logo is attached, it can be used light or dark.
Our only color used is the warm grey Pantone 8003C hex #877A69

You will only need to design the homepage to win the competition, but the winning designer will be required to supply without extra charges:
1. Home page design
2. A second, standard page template design
3. An icon set in colors appropriate to the site that have icons to match the subjects in these pages:
https://trevanly.com.au/products/
https://trevanly.com.au/making-the-switch/
https://trevanly.com.au/why-trevanly/
We will create a single page version of the options on https://trevanly.com.au/solutions/
4.Any images used

Please avoid stock photos that are too common - e.g. smiling woman with headset, try to make the design stand out with simple images and well-designed layout.

Mid-size business clients

It Company

1 page

• Quil logo
• Use Quil color

```html
<!DOCTYPE html>
<html lang="en">
<head>
<meta charset="utf-8">
<title>Quil – IT Support</title>
<link href="https://fonts.googleapis.com/css2?family=Raleway:wght@400;500;600&display=swap" rel="stylesheet">
<style>
:root{
  --stage:#000;
  --brand:#877a69;
  --brand-dark:#5a4c3c;
  --accent:#e8891e;
  --text:#6b6259;
  --muted:#8e857b;
  --band:#f0eeeb;
  --white:#fff;
  --footer-link:#a8998a;
}
*{margin:0;padding:0;box-sizing:border-box}
html,body{width:1200px;height:1200px;overflow:hidden;background:var(--stage);font-family:'Raleway',sans-serif;color:var(--text)}
.page{position:absolute;left:268px;top:0;width:665px;height:1200px;background:var(--white);overflow:hidden}

/* header */
.site-header{position:absolute;left:0;top:0;width:665px;height:66px;background:var(--white);border-bottom:2px solid var(--accent)}
.brand{position:absolute;left:34px;top:18px;display:flex;align-items:center;gap:5px}
.brand-square{width:10px;height:10px;border:1.5px solid var(--brand)}
.brand-name{font-size:20px;font-weight:400;color:var(--brand);letter-spacing:.5px}
.topline{position:absolute;left:554px;top:21px;font-size:7.5px;font-weight:600;color:var(--text);display:flex;align-items:center;gap:10px}
.main-nav{position:absolute;top:40px;left:272px;font-size:7.5px;color:var(--text)}
.main-nav a{position:absolute;white-space:nowrap;text-decoration:none;color:inherit}
.main-nav .current{border:1px solid var(--brand);border-radius:4px;padding:7px 3px;top:-8px;left:0}

/* hero */
.hero{position:absolute;left:0;top:66px;width:665px;height:230px;background:linear-gradient(100deg,#8d8171 0%,#a89b8a 45%,#7e7263 100%)}
.hero h1{position:absolute;left:39px;top:78px;width:360px;font-size:14.5px;font-weight:500;line-height:18px;color:var(--white)}
.hero .btn{position:absolute;left:42px;top:138px;width:95px;height:21px;border:1px solid var(--white);border-radius:4px;color:var(--white);font-size:11px;text-align:center;line-height:19px}

/* section heads */
.sec-title{position:absolute;left:0;width:665px;text-align:center;font-size:15px;font-weight:500;color:var(--text)}
.rule{position:absolute;height:1px;background:var(--brand)}
.rule-mark{position:absolute;width:7px;height:7px;border:1px solid var(--accent)}

.intro p{position:absolute;left:59px;width:550px;font-size:7px;line-height:10px;color:var(--text)}

.services{position:absolute;left:0;top:438px;width:665px;height:205px;background:var(--band)}
.svc-icon{position:absolute;width:54px;height:52px;border-radius:5px;background:var(--brand)}
.svc-title{position:absolute;font-size:7.5px;color:var(--accent)}
.svc-text{position:absolute;width:100px;font-size:5.5px;line-height:7px;color:var(--muted)}

.fibre-visual{position:absolute;left:87px;top:724px;width:231px;height:100px;background:linear-gradient(180deg,#f5f5f3,#dcdcd8);border-radius:6px}
.fibre-text{position:absolute;left:362px;top:752px;width:245px;font-size:7.5px;line-height:12.5px;color:var(--muted)}

.certs{position:absolute;left:0;top:875px;width:665px;height:162px;background:var(--band)}
.certs p{position:absolute;left:0;width:665px;top:76px;text-align:center;font-size:7.5px;color:var(--muted)}
.badge{position:absolute;border-radius:4px}

.site-footer{position:absolute;left:0;top:1037px;width:665px;height:163px;background:var(--brand-dark)}
.foot-col{position:absolute;top:34px;font-size:6.5px;line-height:12.2px;color:var(--footer-link)}
.foot-col h4{font-size:6.5px;font-weight:600;color:#d9d0c4;letter-spacing:.3px}
.foot-brand{position:absolute;left:568px;top:28px;display:flex;align-items:center;gap:4px}
.foot-brand .brand-square{border-color:#c2b7aa}
.foot-brand .brand-name{color:#c2b7aa;font-size:17px}
.copy{position:absolute;left:568px;top:79px;font-size:6.5px;line-height:12px;color:var(--footer-link)}
</style>
</head>
<body>
<div class="page">

  <header class="site-header">
    <div class="brand"><span class="brand-square"></span><span class="brand-name">quil</span></div>
    <div class="topline">
      <span>+61 (2) 8555 0147</span>
      <svg width="10" height="11" viewBox="0 0 10 11" aria-label="Login"><path d="M2.5 5V3.3a2.5 2.5 0 0 1 5 0" fill="none" stroke="#e8891e" stroke-width="1.4"/><rect x="1" y="5" width="8" height="6" rx="1" fill="#e8891e"/><circle cx="5" cy="8" r="1" fill="#fff"/></svg>
    </div>
    <nav class="main-nav">
      <a class="current" href="#">Home</a>
      <a href="#" style="left:44px">IT Support</a>
      <a href="#" style="left:103px">VoIP</a>
      <a href="#" style="left:142px">Internet and Data</a>
      <a href="#" style="left:226px">Cloud hosting</a>
      <a href="#" style="left:302px">About</a>
      <a href="#" style="left:342px">Contact</a>
    </nav>
  </header>

  <section class="hero" role="img" aria-label="Muted warm photo of a laptop on a desk with notebooks and pens">
    <h1>We Provide IT needs with experience in extensive technologies and platforms with a focus on customer service.</h1>
    <div class="btn">Explore More</div>
  </section>

  <section class="intro">
    <h2 class="sec-title" style="top:318px">do IT better</h2>
    <div class="rule" style="left:275px;top:339px;width:90px"></div>
    <div class="rule-mark" style="left:316px;top:336px;background:#fff"></div>
    <p style="top:360px">Not only does Quil have highly qualified people, with certifications from Norvane, Keltrix, National Comms Board amongst others, but importantly we can speak plain English and translate IT questions into a language you can understand and make decisions easier for you.</p>
    <p style="top:390px">We pride ourselves in our skill, integrity and ability to think and act in your best interests - that's what gets us customer referrals time after time. We support the open exchange of ideas in the IT community and put a lot in ourselves.</p>
  </section>

  <section class="services">
    <h2 class="sec-title" style="top:7px">Our Services</h2>
    <div class="rule" style="left:277px;top:29px;width:90px"></div>
    <div class="rule-mark" style="left:318px;top:26px;background:#f0eeeb"></div>

    <div class="svc-icon" style="left:96px;top:47px">
      <svg width="54" height="52" viewBox="0 0 54 52"><g fill="none" stroke="#fff" stroke-width="1.8"><circle cx="27" cy="20" r="7"/><path d="M18 20a9 9 0 0 1 18 0"/><path d="M15 42c0-8 5-12 12-12s12 4 12 12z"/></g></svg>
    </div>
    <div class="svc-title" style="left:169px;top:50px">IT Support</div>
    <div class="svc-text" style="left:169px;top:62px">We speak many languages including plain English, and will make your experience a pleasure from start to finish.</div>

    <div class="svc-icon" style="left:366px;top:49px">
      <svg width="54" height="52" viewBox="0 0 54 52"><g fill="none" stroke="#fff" stroke-width="1.8"><path d="M16 36a8 8 0 0 1 0-16 11 11 0 0 1 21-3 8 8 0 0 1 2 19z"/><rect x="20" y="24" width="14" height="16" rx="1" fill="#877a69"/></g></svg>
    </div>
    <div class="svc-title" style="left:435px;top:49px">VoIP</div>
    <div class="svc-text" style="left:436px;top:61px">We supply a wide range of business data connections which are reliable, scalable, fast and represent excellent value for money.</div>

    <div class="svc-icon" style="left:96px;top:125px">
      <svg width="54" height="52" viewBox="0 0 54 52"><g fill="none" stroke="#fff" stroke-width="1.8"><ellipse cx="25" cy="16" rx="10" ry="4"/><path d="M15 16v20c0 2 4 4 10 4M35 16v8M15 23c0 2 4 4 10 4s10-2 10-4M15 30c0 2 4 4 10 4"/><path d="M36 28l6 2v5c0 4-3 6-6 7-3-1-6-3-6-7v-5z" fill="#fff"/></g></svg>
    </div>
    <div class="svc-title" style="left:164px;top:124px">Internet and Data</div>
    <div class="svc-text" style="left:164px;top:139px">We are specialists in Norvane, fully conversant with Velmac and Orix. We write websites and applications.</div>

    <div class="svc-icon" style="left:366px;top:125px">
      <svg width="54" height="52" viewBox="0 0 54 52"><g fill="none" stroke="#fff" stroke-width="1.8"><path d="M16 36a8 8 0 0 1 0-16 11 11 0 0 1 21-3 8 8 0 0 1 2 19"/><rect x="22" y="22" width="11" height="16" rx="1" fill="#877a69"/><path d="M25 27h5M25 31h5M25 35h5"/></g></svg>
    </div>
    <div class="svc-title" style="left:432px;top:128px">Cloud Hosting</div>
    <div class="svc-text" style="left:432px;top:140px">Quil provides a range of cloud services, including Software as a service, Infrastructure as a service and Platform as a service.</div>
  </section>

  <section class="fibre-offer">
    <h2 class="sec-title" style="top:668px;left:20px">We now offer Fibrelink connections!</h2>
    <div class="rule" style="left:305px;top:693px;width:90px"></div>
    <div class="rule-mark" style="left:346px;top:690px;background:#fff"></div>
    <div class="fibre-visual" role="img" aria-label="Labelled drawing of a Fibrelink connection box with its data and power ports"></div>
    <p class="fibre-text">Connect to the internet or inter-site with incredible speeds of up to 10Gbps! Ultra-reliable and flexible range of options through our simple data product range.</p>
  </section>

  <section class="certs">
    <h2 class="sec-title" style="top:34px;left:-20px">Certified Technicians</h2>
    <div class="rule" style="left:265px;top:56px;width:166px"></div>
    <div class="rule-mark" style="left:344px;top:53px;background:#f0eeeb"></div>
    <p>Be confident that the skills required are available and certified - we have a broad range of expertise and continuously update our skills and certifications</p>
    <div class="badge" style="left:190px;top:98px;width:60px;height:41px;background:#e4e2de"></div>
    <div class="badge" style="left:300px;top:98px;width:50px;height:41px;background:#fff;border:1px solid #9a9288"></div>
    <div class="badge" style="left:414px;top:98px;width:43px;height:41px;background:#1f6f78"></div>
  </section>

  <footer class="site-footer">
    <div class="foot-col" style="left:90px"><h4>COMPANY</h4>About Us<br>Careers<br>Legal Terms<br>Terms of Use<br>Privacy Policy</div>
    <div class="foot-col" style="left:209px"><h4>SERVICES</h4>IT Support<br>VoIP<br>Internet and Data<br>Cloud hosting</div>
    <div class="foot-col" style="left:341px"><h4>PRODUCTS</h4>Corporate Workstations<br>Orchard desktops, laptops and tablets<br>Halden Standalone and Blade Servers<br>Halden and Printwell Printers<br>Maintenance Contracts</div>
    <div class="foot-brand"><span class="brand-square"></span><span class="brand-name">quil</span></div>
    <div class="copy">Copyright © 2017<br>All Rights Reserved.</div>
  </footer>

</div>
</body>
</html>
```